Brenton Wealth Management Flow Charts

I need help creating three flow charts for my businesses website. We want them to be simple but look professional. This is for a Wealth Management firm. I will attach a word document that has all of the descriptions for everything so you know what icons to use. We just want the chart to have an icon, the names of each step and the corresponding numbers. I will also include some examples of charts we liked as well. Once the winner is selected, we will need help with additional graphic design elements for our website ASAP.
- Goudy Roman

```html
<!DOCTYPE html>
<html lang="en">
<head>
<meta charset="utf-8">
<title>Retirement Planning Process</title>
<link rel="stylesheet" href="https://fonts.googleapis.com/css2?family=Bowlby+One&family=Arimo:wght@400&family=Oswald:wght@700&display=swap">
<style>
  :root {
    --ink: #111111;
    --label: #1e1e1e;
    --tile: #dfe3da;
    --wedge: #cbcbcb;
    --wedge-edge: #d9d9d9;
    --badge: #e4e4e4;
    --target-red: #c8102e;
    --arc-1: #f0505a;
    --arc-2: #c0182a;
    --arc-3: #8b0f1a;
    --step-1: #cfe07a;
    --step-2: #93b04a;
    --step-3: #7aaa3e;
    --step-4: #5f9f3a;
    --step-5: #4a9638;
    --step-6: #3a8c32;
  }
  html, body { margin: 0; padding: 0; overflow: hidden; background: #ffffff; }
  .canvas { position: relative; width: 1200px; height: 1000px; overflow: hidden; background: #ffffff; }
  .artwork { position: absolute; left: 0; top: 0; }
  .heading {
    position: absolute; margin: 0; font-family: "Bowlby One", "Arial Black", sans-serif;
    font-weight: 400; color: var(--ink); line-height: 1.25; text-align: center;
  }
  .process-title { left: 0; width: 1200px; top: 26px; font-size: 37px; letter-spacing: 0.5px; }
  .legacy-title { left: 850px; width: 300px; top: 436px; font-size: 26px; line-height: 1.6; }
  .step-label {
    position: absolute; top: 270px; margin: 0; font-family: "Arimo", Arial, sans-serif;
    font-size: 23px; color: var(--label); line-height: 1.3;
  }
  .step-label .wrap { display: block; padding-left: 28px; }
  .wedge-label { font-family: "Arimo", Arial, sans-serif; font-size: 18px; fill: var(--label); text-anchor: middle; }
  .arc-word { font-family: "Oswald", "Arial Narrow", sans-serif; font-weight: 700; text-anchor: middle; letter-spacing: 1px; }
  .estate-label { font-family: "Arimo", Arial, sans-serif; font-size: 21px; fill: var(--label); }
  .line-icon { fill: none; stroke: #333; stroke-width: 2.5; stroke-linecap: round; stroke-linejoin: round; }
</style>
</head>
<body>
<div class="canvas">
  <svg class="artwork" width="1200" height="1000" viewBox="0 0 1200 1000" xmlns="http://www.w3.org/2000/svg">
    <defs>
      <g id="person">
        <circle cx="0" cy="-6" r="6" fill="#f2f2f2" stroke="#333" stroke-width="2"/>
        <path d="M-11 10 Q-11 1 0 1 Q11 1 11 10 Z" fill="#f2f2f2" stroke="#333" stroke-width="2"/>
      </g>
      <polygon id="star" points="0,-12 2.9,-4 11.4,-3.7 4.8,1.5 7.1,9.7 0,5 -7.1,9.7 -4.8,1.5 -11.4,-3.7 -2.9,-4" fill="#f5c518" stroke="#333" stroke-width="1.3"/>
      <path id="wedge" d="M-6 -10 L-88 -238 Q0 -258 88 -238 L6 -10 Z"/>
      <path id="arc-outer" d="M23 760 A285 285 0 0 1 593 760"/>
      <path id="arc-middle" d="M63 760 A245 245 0 0 1 553 760"/>
      <path id="arc-inner" d="M108 760 A200 200 0 0 1 508 760"/>
      <linearGradient id="fade-red" x1="0" x2="1"><stop offset="0" stop-color="#fbe3e3"/><stop offset=".9" stop-color="#fbe3e3"/><stop offset="1" stop-color="#fbe3e3" stop-opacity="0"/></linearGradient>
      <linearGradient id="fade-mint" x1="0" x2="1"><stop offset="0" stop-color="#e2fbf6"/><stop offset=".9" stop-color="#e2fbf6"/><stop offset="1" stop-color="#e2fbf6" stop-opacity="0"/></linearGradient>
      <linearGradient id="fade-sky" x1="0" x2="1"><stop offset="0" stop-color="#e1eefc"/><stop offset=".9" stop-color="#e1eefc"/><stop offset="1" stop-color="#e1eefc" stop-opacity="0"/></linearGradient>
      <linearGradient id="fade-aqua" x1="0" x2="1"><stop offset="0" stop-color="#e0f2f4"/><stop offset=".9" stop-color="#e0f2f4"/><stop offset="1" stop-color="#e0f2f4" stop-opacity="0"/></linearGradient>
      <linearGradient id="fade-grey" x1="0" x2="1"><stop offset="0" stop-color="#e4e4e4"/><stop offset=".9" stop-color="#e4e4e4"/><stop offset="1" stop-color="#e4e4e4" stop-opacity="0"/></linearGradient>
    </defs>

    <g class="process-band">
      <rect x="150" y="140" width="110" height="112" rx="14" fill="var(--step-1)"/>
      <rect x="345" y="140" width="110" height="112" rx="14" fill="var(--step-2)"/>
      <rect x="540" y="140" width="110" height="112" rx="14" fill="var(--step-3)"/>
      <rect x="734" y="140" width="110" height="112" rx="14" fill="var(--step-4)"/>
      <rect x="928" y="140" width="110" height="112" rx="14" fill="var(--step-5)"/>
      <polygon points="1010,138 1122,138 1122,108 1168,180 1122,252 1010,252" fill="var(--step-6)" stroke="#222" stroke-width="3"/>
    </g>

    <g class="process-tiles">
      <rect x="46" y="122" width="122" height="115" rx="12" fill="#222"/>
      <rect x="42" y="118" width="122" height="115" rx="12" fill="var(--tile)"/>
      <rect x="239" y="122" width="122" height="115" rx="12" fill="#222"/>
      <rect x="235" y="118" width="122" height="115" rx="12" fill="var(--tile)"/>
      <rect x="434" y="122" width="122" height="115" rx="12" fill="#222"/>
      <rect x="430" y="118" width="122" height="115" rx="12" fill="var(--tile)"/>
      <rect x="628" y="122" width="122" height="115" rx="12" fill="#222"/>
      <rect x="624" y="118" width="122" height="115" rx="12" fill="var(--tile)"/>
      <rect x="822" y="122" width="122" height="115" rx="12" fill="#222"/>
      <rect x="818" y="118" width="122" height="115" rx="12" fill="var(--tile)"/>
      <rect x="1019" y="122" width="110" height="115" rx="12" fill="#222"/>
      <rect x="1015" y="118" width="110" height="115" rx="12" fill="var(--tile)"/>
    </g>

    <g class="icon-discovery" transform="translate(103 175)">
      <circle r="26" class="line-icon"/>
      <use href="#person" transform="translate(0 -24)"/>
      <use href="#person" transform="translate(-24 16)"/>
      <use href="#person" transform="translate(24 16)"/>
    </g>
    <g class="icon-learning" transform="translate(296 175)">
      <line x1="10" y1="10" x2="28" y2="30" stroke="#333" stroke-width="7" stroke-linecap="round"/>
      <circle cx="-5" cy="-5" r="22" fill="#9ab8e0" stroke="#333" stroke-width="3"/>
      <circle cx="-5" cy="-15" r="2.5" fill="#333"/>
      <line x1="-5" y1="-8" x2="-5" y2="8" stroke="#333" stroke-width="4"/>
    </g>
    <g class="icon-planning" transform="translate(491 175)">
      <rect x="-24" y="-32" width="44" height="62" rx="3" fill="#fff" stroke="#333" stroke-width="2.5"/>
      <path d="M-16 -20 H12 M-16 -12 H12 M-16 -4 H12 M-16 4 H12 M-16 12 H4" class="line-icon" stroke-width="2"/>
      <line x1="10" y1="22" x2="28" y2="-18" stroke="#333" stroke-width="4" stroke-linecap="round"/>
      <path d="M10 22 L8 28 L13 24 Z" fill="#333"/>
    </g>
    <g class="icon-execution" transform="translate(685 177)">
      <rect x="-24" y="-30" width="48" height="62" rx="4" fill="#fff" stroke="#333" stroke-width="2.5"/>
      <rect x="-11" y="-37" width="22" height="11" rx="2" fill="#8b5a3c" stroke="#333" stroke-width="1.5"/>
      <path d="M-17 -14 l3 3 l5 -6 M-17 0 l3 3 l5 -6 M-17 14 l3 3 l5 -6" class="line-icon" stroke-width="2"/>
      <path d="M-4 -13 H14 M-4 1 H14 M-4 15 H10" class="line-icon" stroke-width="2"/>
      <line x1="8" y1="24" x2="30" y2="-10" stroke="#333" stroke-width="4" stroke-linecap="round"/>
    </g>
    <g class="icon-alignment" transform="translate(879 175)">
      <circle cx="-6" cy="0" r="15" fill="none" stroke="#333" stroke-width="7" stroke-dasharray="5 4"/>
      <circle cx="-6" cy="0" r="11" class="line-icon"/>
      <circle cx="-6" cy="0" r="5" class="line-icon"/>
      <line x1="6" y1="16" x2="26" y2="-8" stroke="#333" stroke-width="4" stroke-linecap="round"/>
    </g>
    <g class="icon-review" transform="translate(1072 176)">
      <use href="#star" transform="translate(0 -24) scale(1.1)"/>
      <use href="#star" transform="translate(23 -7) scale(1.1)"/>
      <use href="#star" transform="translate(14 20) scale(1.1)"/>
      <use href="#star" transform="translate(-14 20) scale(1.1)"/>
      <use href="#star" transform="translate(-23 -7) scale(1.1)"/>
    </g>

    <g class="wheel" transform="translate(308 708)" fill="var(--wedge)" stroke="var(--wedge-edge)" stroke-width="2" stroke-linejoin="round">
      <use href="#wedge" transform="rotate(51.4)"/>
      <use href="#wedge" transform="rotate(102.8)"/>
      <use href="#wedge" transform="rotate(154.2)"/>
      <use href="#wedge" transform="rotate(205.8)"/>
      <use href="#wedge" transform="rotate(257.2)"/>
      <use href="#wedge" transform="rotate(308.6)"/>
    </g>

    <g class="wheel-title">
      <text class="arc-word" font-size="30" fill="var(--arc-1)"><textPath href="#arc-outer" startOffset="50%">COMPREHENSIVE</textPath></text>
      <text class="arc-word" font-size="26" fill="var(--arc-2)"><textPath href="#arc-middle" startOffset="50%">INVESTMENT</textPath></text>
      <text class="arc-word" font-size="21" fill="var(--arc-3)"><textPath href="#arc-inner" startOffset="50%">MANAGEMENT</textPath></text>
    </g>

    <g class="target" transform="translate(308 708)">
      <circle r="86" fill="#f4f4f4"/>
      <circle r="80" fill="var(--target-red)"/>
      <circle r="63" fill="#fff"/>
      <circle r="46" fill="var(--target-red)"/>
      <circle r="30" fill="#fff"/>
      <circle r="16" fill="var(--target-red)"/>
    </g>

    <g class="wedge-labels">
      <text class="wedge-label"><tspan x="183" y="574">1</tspan><tspan x="183" y="598">Understanding</tspan><tspan x="173" y="621">your Risk</tspan><tspan x="183" y="644">Tolerance</tspan></text>
      <text class="wedge-label"><tspan x="428" y="563">6</tspan><tspan x="428" y="587">Behavior</tspan><tspan x="428" y="611">Finance</tspan><tspan x="428" y="636">Coaching</tspan></text>
      <text class="wedge-label"><tspan x="153" y="704">2</tspan><tspan x="153" y="730">Investment</tspan><tspan x="153" y="754">Selection</tspan></text>
      <text class="wedge-label"><tspan x="460" y="704">5</tspan><tspan x="460" y="730">Distribution</tspan><tspan x="460" y="754">Strategy</tspan></text>
      <text class="wedge-label"><tspan x="238" y="817">3</tspan><tspan x="238" y="842">Asset</tspan><tspan x="238" y="867">Allocation</tspan></text>
      <text class="wedge-label"><tspan x="370" y="814">4</tspan><tspan x="370" y="839">Tax</tspan><tspan x="370" y="864">efficiency</tspan></text>
    </g>

    <g class="wheel-badges">
      <circle cx="120" cy="540" r="38" fill="var(--badge)"/>
      <g transform="translate(120 540)">
        <path d="M0 -28 Q10 -14 10 -8 A10 10 0 0 1 -10 -8 Q-10 -14 0 -28 Z" fill="#3a8fd8"/>
        <circle cx="0" cy="4" r="6" fill="#1f6fb8"/>
        <path d="M-20 6 Q-20 24 0 24 Q20 24 20 6 L14 6 Q14 16 0 16 Q-14 16 -14 6 Z" fill="#1f6fb8"/>
        <rect x="-6" y="12" width="12" height="16" fill="#1f6fb8"/>
      </g>
      <circle cx="508" cy="545" r="38" fill="var(--badge)"/>
      <g transform="translate(508 545)">
        <rect x="-20" y="-20" width="40" height="28" fill="#fff" stroke="#1a9a9a" stroke-width="3"/>
        <path d="M-4 2 L4 -6 L10 -2 L16 -12" fill="none" stroke="#1a9a9a" stroke-width="2.5"/>
        <circle cx="-14" cy="-4" r="5" fill="#1a9a9a"/>
        <path d="M-22 22 V10 Q-22 4 -14 4 Q-6 4 -6 10 V22 Z" fill="#1a9a9a"/>
      </g>
      <circle cx="60" cy="745" r="38" fill="var(--badge)"/>
      <g transform="translate(60 745)" fill="none" stroke="#f08a1c" stroke-width="6" stroke-linecap="round" stroke-linejoin="round">
        <path d="M0 26 V-4 L-16 -4 M0 -4 V-22 M0 -4 L16 -4"/>
        <path d="M-10 -10 L-18 -4 L-10 2 M10 -10 L18 -4 L10 2 M-6 -16 L0 -24 L6 -16"/>
      </g>
      <circle cx="557" cy="745" r="38" fill="var(--badge)"/>
      <g transform="translate(557 745)">
        <path d="M0 0 L-18 -14 M0 0 L16 -16 M0 0 L20 8 M0 0 L-4 20 M0 0 L-20 10" stroke="#e8c400" stroke-width="2.5"/>
        <circle r="7" fill="#f5d800"/>
        <circle cx="-18" cy="-14" r="4.5" fill="#f5d800"/><circle cx="16" cy="-16" r="4.5" fill="#f5d800"/>
        <circle cx="20" cy="8" r="4.5" fill="#f5d800"/><circle cx="-4" cy="20" r="4.5" fill="#f5d800"/>
        <circle cx="-20" cy="10" r="4.5" fill="#f5d800"/>
      </g>
      <circle cx="200" cy="920" r="38" fill="var(--badge)"/>
      <g transform="translate(200 920)">
        <circle r="24" fill="#2e6e2e"/>
        <path d="M0 0 V-24 M0 0 L20 13 M0 0 L-21 11" stroke="#e4e4e4" stroke-width="2.5"/>
        <text x="-8" y="-6" font-family="Arimo, Arial, sans-serif" font-size="12" fill="#e4e4e4" text-anchor="middle">$</text>
      </g>
      <circle cx="418" cy="928" r="38" fill="var(--badge)"/>
      <g transform="translate(418 928)">
        <rect x="-17" y="-22" width="34" height="40" rx="2" fill="#fff" stroke="#c8202a" stroke-width="3"/>
        <path d="M-10 -14 H10 M-10 -8 H10" stroke="#c8202a" stroke-width="2"/>
        <rect x="-20" y="0" width="40" height="14" fill="#c8202a"/>
        <text x="0" y="11" font-family="Arimo, Arial, sans-serif" font-size="11" fill="#fff" text-anchor="middle">TAX</text>
      </g>
    </g>

    <g class="estate-panels">
      <rect x="832" y="527" width="340" height="72" fill="url(#fade-red)"/>
      <rect x="832" y="607" width="340" height="72" fill="url(#fade-mint)"/>
      <rect x="832" y="687" width="340" height="72" fill="url(#fade-sky)"/>
      <rect x="832" y="767" width="340" height="72" fill="url(#fade-aqua)"/>
      <rect x="832" y="847" width="340" height="72" fill="url(#fade-grey)"/>
      <text class="estate-label" x="840" y="570">1. Beneficiaries</text>
      <text class="estate-label" x="840" y="650">2. Trusts</text>
      <text class="estate-label" x="840" y="728">3. Estate Taxes and Assessment</text>
      <text class="estate-label" x="840" y="806">4. Annual Giving</text>
      <text class="estate-label" x="840" y="885">5. Donations and Charity</text>
    </g>

    <g class="estate-stack">
      <polygon points="662,525 705,455 782,452 735,495 735,533" fill="#e3a24e"/>
      <polygon points="735,533 735,495 782,452 830,495 830,533" fill="#f7dc8a"/>
      <use href="#star" transform="translate(778 500) scale(1.7)"/>
      <polygon points="662,525 735,533 735,613 662,605" fill="#b86a5a"/>
      <rect x="735" y="533" width="95" height="80" fill="#e07474"/>
      <polygon points="662,605 735,613 735,693 662,685" fill="#6aa8c8"/>
      <rect x="735" y="613" width="95" height="80" fill="#7ecbd8"/>
      <polygon points="662,685 735,693 735,773 662,765" fill="#5f8fce"/>
      <rect x="735" y="693" width="95" height="80" fill="#8aaee8"/>
      <polygon points="662,765 735,773 735,853 662,845" fill="#5a6fa8"/>
      <rect x="735" y="773" width="95" height="80" fill="#7493c4"/>
      <polygon points="662,845 735,853 735,933 662,925" fill="#9a9a9a"/>
      <rect x="735" y="853" width="95" height="80" fill="#e8e8e8"/>

      <g transform="translate(782 573)" fill="#222">
        <path d="M-22 -6 A22 16 0 0 1 22 -6 Z"/>
        <line x1="0" y1="-6" x2="0" y2="6" stroke="#222" stroke-width="2"/>
        <circle cx="-12" cy="6" r="4"/><rect x="-16" y="11" width="8" height="16" rx="3"/>
        <circle cx="12" cy="6" r="4"/><rect x="8" y="11" width="8" height="16" rx="3"/>
        <circle cx="0" cy="12" r="3"/><rect x="-3" y="16" width="6" height="11" rx="2"/>
      </g>
      <g transform="translate(782 653)">
        <path d="M2 -26 L18 -20 V-6 Q18 6 2 12 Q-14 6 -14 -6 V-20 Z" fill="none" stroke="#222" stroke-width="3"/>
        <path d="M-5 -8 L0 -3 L9 -13" fill="none" stroke="#222" stroke-width="3"/>
        <path d="M-24 14 L-10 6 L4 14 L-6 24 Z M24 14 L10 6 L-2 16 L8 24 Z" fill="#222"/>
      </g>
      <g transform="translate(782 733)">
        <rect x="-12" y="-26" width="30" height="40" rx="2" fill="none" stroke="#222" stroke-width="2.5"/>
        <rect x="-6" y="-6" width="26" height="12" fill="#222"/>
        <text x="7" y="4" font-family="Arimo, Arial, sans-serif" font-size="10" fill="#fff" text-anchor="middle">TAX</text>
        <circle cx="-14" cy="12" r="9" fill="none" stroke="#222" stroke-width="3"/>
        <line x1="-20" y1="19" x2="-26" y2="26" stroke="#222" stroke-width="4" stroke-linecap="round"/>
      </g>
      <g transform="translate(782 813)" fill="#222">
        <rect x="-6" y="-24" width="22" height="18"/>
        <rect x="-8" y="-28" width="26" height="6"/>
        <path d="M-24 4 H-8 Q4 4 10 8 L22 2 Q26 2 24 8 L10 18 H-14 V22 H-24 Z"/>
      </g>
      <g transform="translate(782 893)">
        <text x="0" y="-18" font-family="Arimo, Arial, sans-serif" font-size="10" fill="#222" text-anchor="middle" transform="rotate(-8)">DONATE</text>
        <path d="M0 -12 V2 M-4 -2 L0 2 L4 -2" fill="none" stroke="#222" stroke-width="2"/>
        <path d="M-18 6 L0 0 L18 6 L18 24 L0 30 L-18 24 Z M-18 6 L0 12 L18 6 M0 12 V30" fill="none" stroke="#222" stroke-width="2.2" stroke-linejoin="round"/>
      </g>
    </g>
  </svg>

  <h1 class="heading process-title">THE RETIREMENT PLANNING PROCESS</h1>
  <p class="step-label" style="left:25px">1. Discovery<span class="wrap">Meeting</span></p>
  <p class="step-label" style="left:228px">2. Learning</p>
  <p class="step-label" style="left:422px">3. Planning</p>
  <p class="step-label" style="left:610px">4. Execution</p>
  <p class="step-label" style="left:812px">5. Alignment</p>
  <p class="step-label" style="left:1016px">6. Review</p>

  <h2 class="heading legacy-title">LEGACY AND<br>ESTATE PLANNING</h2>
</div>
</body>
</html>
```